LeaseWiser - Apartment Reviews Website Concept Sketch

IMPORTANT UPDATES BELOW -

Current Contest:
Deliverable: 1 or more original design concepts for website home-page. A guaranteed payment will be made to the lead design.

Context:
This guaranteed-payment contest is for submission of 1 or more concept sketches for the home page of the website described below.

Based on finalist submissions, a freelance contract may be let for design-only development (PSDs only) of the full site, approximately 20 pages. Budget for the full site design is $3000 - $5000 and will include multiple rounds to refine the home-page concept and then to extend the design to the full site.

All mySql and PHP logic is already coded and working. No coding is required for the contest or the follow-on project.

IMPORTANT UPDATES ABOVE -

The Website:

LeaseWiser is developing an on-line, searchable, pay-for-access database of user-contributed reviews of apartment complexes. Consumers will use these reviews to make better informed decisions before committing to an apartment lease.

We currently have a functional, wireframe-only website accessible at leasewiser.example. The wireframes are under development, and site pages may display debugging information or may be inaccessible on occasion.

Additional information as well as a site map is available at: leasewiser.example/qqstudio.

We require complete graphic design for a multi-page, interactive, database-driven website. Cutting and coding the design into the existing php code base is a separate project, but feel free to quote on this separately if you have capabilities. We do not require any software or database development. All software is proprietary, we are not using any third-party platform for CMS, survey management, etc.

Attributes we wish to convey with our logo, website, and other presentation:
• Trustworthiness – users should expect the information we present to be accurate and complete
• Impartiality - users can rely on the survey results we present not to be influenced or “bought” by apartment managers
• Professionalism – LeaseWiser is a team of professionals dedicated to building and delivering a high-value, high-relevance database of fresh information that will help apartment renters make better decisions about where to live. We are not an informal community, not a group of volunteers, and not a free-access, open source product.
• Simplicity – our site is easy to use, easy to search, and our survey results are easy to understand
• Accessibility – anyone can use our service, it is not just for experts or people with technical skills
• Affordability – our service is priced at a point (about $50 for 90-days use) that it is affordable for everyone who plans to rent an apartment and makes economic sense as insurance against making an uninformed decision (much less than the cost of a month’s rent)
• Interest to Apartment Dwellers – our name, and preferably our logo, identifies us immediately as being of interest to apartment renters and seekers
• Positive Outlook – although the greatest value of LeaseWiser will be in helping apartment hunters avoid buildings with construction, management, and neighborhood problems, our website imagery should not focus on the negative aspects, but rather on the happiness, security, and satisfaction that comes with a good selection of an apartment

Website Purpose
During Phase 1 (current) of LeaseWiser’s development, the purpose of the website is to collect apartment reviews. Traffic will be driven by a display/performance ad campaign. We are assembling a business asset (the database) and this is really a direct response marketing campaign. We will offer a variety of incentives (sweepstakes entries, gift card redemption) to induce people to complete a survey and view a series of advertising offers. During Phase 1, there will be no database of apartment reviews for users to preview, and nothing for us to sell.

During Phase 2 (future) of LeaseWiser’s development, the purpose of the website will be to induce members to pay to access the database, and to provide a means for paying customers to access the database of reviews. Phase 2 is NOT in scope at this time, but will represent a substantial future upgrade - naturally the original design team will be in a strong competitive position for this future work.

The LeaseWiser website has a small area that will serve our advertising partners so they can access campaign and reporting information. This part of the site will need a simple but professional design treatment and is within the scope of Phase 1 development.

Our primary creative goal at this time is to present a website that supports Phase 1 goals. Many of the pages necessary for Phase 2 operation are outside the scope of the Phase 1 creative effort, in particular previewing reviews, searching the database, viewing search results, and transaction-oriented pages.
Updates

Project Deadline Extended
Reason: We didn't communicate the nature of the Design Contest well. We are extending the deadline to permit designers to re-evaluate the scope of the current work in the context of the award amount.

Target Market(s)

Our market audience is internet-savvy Americans who live in or are moving into an apartment.

Industry/Entity Type

Graphic Design

Requirements
Must have
• We are finalizing logo design and have posted a draft copy on the site. Logo design is still subject to refinement, but the basic concept is frozen. Colors / combinations may change, but will be arena of blue or blue+green.

Key elements of the home page are:
- a call to action to review an apartment
- room for 1-2 rotating articles about selecting an apartment, planning a move, shopping for insurance in your new location, etc. to act as light-weight, added value elements for site visitors.

Important to know:
- The survey itself (reviewapartment.php - only accessible by following all the steps starting with the "review an apartment" link) is database-driven, so the design must be able to accommodate assembly of questions in different formats using a building-block approach. The current wire-frame illustrates the major question/answer formats: radio; checkbox; matrix-radio; free-text.

Over the life of the project, we will undoubtedly build dozens of landing pages that center around the call to action of "review the apartment where you live" with various inducements (sweepstakes entry, redeemable incentives, social appeals, etc.) Development of these landing pages is a separate project, but the initial design should include one or two. If direct-marketing design / landing page design is not your forte, these pages can be removed from the scope of the web design project.

Should not have
• We would prefer to stay away from flash-heavy pages for the website.

```html
<!DOCTYPE html>
<html lang="en">
<head>
<meta charset="utf-8">
<title>LeaseWiser – Home</title>
<link rel="stylesheet" href="https://fonts.googleapis.com/css2?family=Noto+Sans:wght@400&family=Arimo:wght@400;700&family=Carlito&display=swap">
<style>
  :root {
    --bg-top: #ffffff;
    --bg-bottom: #dbeefc;
    --brand-orange: #e0622a;
    --ink: #222222;
    --nav-ink: #4a4a12;
    --rule: #d6d6d6;
    --accent-blue: #12709f;
    --heading-blue: #1d46a8;
    --panel-white: #ffffff;
    --panel-grey: #e1e1e1;
    --footer-bg: #1b1b19;
    --footer-ink: #ffffff;
    --hero-a: #e8ddcf;
    --hero-b: #b79a78;
  }
  * { box-sizing: border-box; margin: 0; padding: 0; }
  html, body { width: 1200px; height: 900px; overflow: hidden; }
  body {
    position: relative;
    background: linear-gradient(to bottom, var(--bg-top) 0, var(--bg-top) 60px, var(--bg-bottom) 800px);
    font-family: "Arimo", Arial, sans-serif;
    color: var(--ink);
  }
  .topbar {
    position: absolute; left: 0; top: 0; width: 1200px; height: 36px;
    border-bottom: 1px solid var(--rule); background: var(--bg-top);
  }
  .topbar__links {
    position: absolute; right: 85px; top: 18px;
    font-family: "Noto Sans", Verdana, sans-serif; font-size: 13px; color: var(--ink);
    display: flex; gap: 19px;
  }
  .brand {
    position: absolute; left: 88px; top: 64px;
    font-family: "Noto Sans", Verdana, sans-serif; font-size: 39px; color: var(--brand-orange);
  }
  .site-search {
    position: absolute; left: 930px; top: 104px; width: 210px; height: 27px;
    border-radius: 14px; border: 1px solid #c4c4c4;
    background: linear-gradient(#f2f2f2, #dadada);
    font-family: "Arimo", Arial, sans-serif; font-size: 12px; color: #777;
    padding: 6px 11px;
  }
  .site-search svg { position: absolute; right: 4px; top: 3px; }
  .main-nav {
    position: absolute; left: 79px; top: 163px; width: 1069px; height: 47px;
    border: 1px solid #c9d2d8; border-radius: 8px; background: var(--panel-white);
    display: flex; align-items: center; padding-left: 22px;
    font-family: "Noto Sans", Verdana, sans-serif; font-size: 13px; color: var(--nav-ink);
  }
  .main-nav__item { padding: 0 14px; height: 47px; line-height: 47px; border-right: 1px solid #e2e2e2; }
  .main-nav__item:last-child { border-right: none; }
  .hero {
    position: absolute; left: 80px; top: 224px; width: 761px; height: 328px;
    background: linear-gradient(100deg, #f1ece4 0%, var(--hero-a) 35%, var(--hero-b) 70%, #8f7a62 100%);
  }
  .finder {
    position: absolute; left: 854px; top: 223px; width: 285px; height: 329px;
    background: var(--panel-white); border-radius: 6px;
  }
  .finder__title {
    position: absolute; left: 26px; top: 17px;
    font-family: "Noto Sans", Verdana, sans-serif; font-size: 19px; color: var(--ink);
  }
  .finder__field {
    position: absolute; left: 22px; width: 248px; height: 34px;
    border: 1px solid #9c9c9c; background: var(--panel-white);
  }
  .finder__button {
    position: absolute; left: 173px; top: 248px; width: 96px; height: 35px;
    background: var(--accent-blue); color: #fff; border-radius: 7px;
    font-family: "Noto Sans", Verdana, sans-serif; font-size: 18px;
    text-align: center; line-height: 35px;
  }
  .welcome__title {
    position: absolute; left: 80px; top: 584px;
    font-size: 18px; color: var(--heading-blue);
  }
  .welcome__text {
    position: absolute; left: 101px; top: 621px; width: 722px;
    font-size: 12.5px; line-height: 20px; color: var(--ink);
  }
  .welcome__button {
    position: absolute; left: 391px; top: 707px; width: 92px; height: 41px;
    background: var(--accent-blue); color: #fff; font-weight: 700; font-size: 13px;
    text-align: center; line-height: 41px;
  }
  .newsletter {
    position: absolute; left: 857px; top: 573px; width: 281px; height: 162px;
    background: var(--panel-grey); border-radius: 5px;
  }
  .newsletter__tab {
    position: absolute; left: -12px; top: 10px; width: 262px; height: 38px;
    border-radius: 0 10px 10px 10px;
    background: linear-gradient(#ffffff, #d9d9d9);
    box-shadow: 0 2px 2px rgba(0,0,0,.2);
    font-family: "Carlito", Calibri, sans-serif; font-size: 25px; color: var(--ink);
    text-align: center; line-height: 38px;
  }
  .newsletter__fold {
    position: absolute; left: -12px; top: 48px; width: 12px; height: 10px;
    background: #24504e; border-radius: 0 0 0 10px;
  }
  .newsletter__text {
    position: absolute; left: 14px; top: 53px; width: 250px;
    font-family: "Carlito", Calibri, sans-serif; font-size: 15.5px; line-height: 20px; color: #555;
  }
  .newsletter__input {
    position: absolute; left: 12px; top: 116px; width: 185px; height: 34px;
    background: #fafafa; border: 1px solid #cfcfcf; border-radius: 5px;
  }
  .newsletter__submit {
    position: absolute; left: 203px; top: 116px; width: 54px; height: 34px;
    background: linear-gradient(#4a4a4a, #2a2a2a); border-radius: 5px;
  }
  .newsletter__submit svg { position: absolute; left: 17px; top: 8px; }
  .footer {
    position: absolute; left: 0; top: 803px; width: 1200px; height: 97px;
    background: var(--footer-bg); color: var(--footer-ink);
  }
  .footer__social { position: absolute; left: 85px; top: 31px; display: flex; gap: 11px; }
  .footer__social-item { width: 32px; height: 32px; border-radius: 5px; background: #5d7aa6; }
  .footer__links {
    position: absolute; left: 545px; width: 560px; top: 24px;
    font-size: 11px; text-align: center; line-height: 20px;
  }
</style>
</head>
<body>
  <header class="topbar">
    <nav class="topbar__links"><span>Log In</span><span>Register</span></nav>
  </header>

  <div class="brand">LeaseWiser</div>

  <div class="site-search">search...
    <svg width="20" height="20" viewBox="0 0 20 20" aria-hidden="true">
      <circle cx="10" cy="10" r="9" fill="#8a8a8a"/>
      <circle cx="9" cy="9" r="4" fill="none" stroke="#fff" stroke-width="1.8"/>
      <line x1="12" y1="12" x2="15" y2="15" stroke="#fff" stroke-width="2"/>
    </svg>
  </div>

  <nav class="main-nav">
    <span class="main-nav__item">Review an apartment</span>
    <span class="main-nav__item">look up apartments</span>
    <span class="main-nav__item">My account</span>
    <span class="main-nav__item">Enter sweeps</span>
    <span class="main-nav__item">Faq &nbsp;t&amp;c</span>
    <span class="main-nav__item">Contest rules</span>
    <span class="main-nav__item">LP View</span>
    <span class="main-nav__item">Survey Complete</span>
    <span class="main-nav__item">Home</span>
  </nav>

  <div class="hero" role="img" aria-label="Photo of a bright modern apartment living room with armchairs, glass table and wood wall unit"></div>

  <section class="finder">
    <h2 class="finder__title" style="font-weight:400">Find and rate</h2>
    <div class="finder__field" style="top:67px"></div>
    <div class="finder__field" style="top:111px"></div>
    <div class="finder__field" style="top:154px"></div>
    <div class="finder__field" style="top:197px"></div>
    <div class="finder__button">Search</div>
  </section>

  <section class="welcome">
    <h1 class="welcome__title" style="font-weight:400">Welcome to our ......</h1>
    <p class="welcome__text">Lorem ipsum dolor sit amet, consectetur adipiscing elit. Praesent tempor facilisis congue. Lorem sum dolor sit amet, consectetur adippend.Lorem ipsum dolor sit amet, consectetur adipiscing elit. Praesent tempor facilisis congue. Lorem sum dolor sit amet, consectetur adippend..Lorem ipsum dolor sit amet, consectetur adipiscing elit. Praesent tempor facilisis congue. Lorem sum dolor sit amet, consectetur adippend..Lorem ipsum dolor sit amet, consectetur adipiscing elit. Praesent tempor facilisis congue. Lorem sum dolor sit amet, consectetur adippend..</p>
    <div class="welcome__button">Learn More</div>
  </section>

  <aside class="newsletter">
    <div class="newsletter__fold"></div>
    <div class="newsletter__tab">Newsletter</div>
    <p class="newsletter__text">Pentru inscriere in newsletter-ul nostru scrieti adresa de e-mail si pasati butonul de inscriere.</p>
    <div class="newsletter__input"></div>
    <div class="newsletter__submit">
      <svg width="20" height="18" viewBox="0 0 20 18" aria-hidden="true">
        <path d="M4 1 L13 9 L4 17" fill="none" stroke="#1fb3d0" stroke-width="4"/>
      </svg>
    </div>
  </aside>

  <footer class="footer">
    <div class="footer__social">
      <span class="footer__social-item" style="background:#5fc4e0"></span>
      <span class="footer__social-item" style="background:#4a65a0"></span>
      <span class="footer__social-item" style="background:#6a7a94"></span>
      <span class="footer__social-item" style="background:#2f7fb5"></span>
      <span class="footer__social-item" style="background:#4c5d78"></span>
    </div>
    <div class="footer__links">
      Home | My Profile | FAQ &nbsp;/ Terms of Use | Privacy Policy | Contest Rules &nbsp;/ About Us | Business Opportunities<br>
      © Copyright 2011, 2012 LeaseWiser, LLC
    </div>
  </footer>
</body>
</html>
```